Create Lanternfield HR Business Cards.

Create Business Cards for Lanternfield HR. 2 sided and Would like the back to have the logo.

Info for Business Card:
Address: 4827 Millbrook Ave Suite 230 Cleveland, Ohio 44987
Office Number: 216-555-0143
Mobile: 216-555-0192

Website: www.lanternfieldhr.example

Target Market(s)

Small to medium size businesses

Industry/Entity Type

Human Resources

Contact Information for Business Card

Company logo and information

Font styles to use
Serif
Sans Serif

Requirements
Must have
• Info for Business Card: Address: 4827 Millbrook Ave Suite 230 Cleveland, Ohio 44987 Office Number: 216-555-0143 Mobile: 216-555-0192 Website: www.lanternfieldhr.example

```html
<!DOCTYPE html>
<html lang="en">
<head>
<meta charset="utf-8">
<title>Lanternfield HR Business Cards</title>
<link rel="stylesheet" href="https://fonts.googleapis.com/css2?family=Open+Sans:wght@400;600;700&display=swap">
<style>
  :root {
    --navy: #29235f;
    --orange: #f28522;
    --white: #ffffff;
    --ink: #2b2b2b;
    --backdrop: #8f8f8f;
  }
  * { margin: 0; padding: 0; box-sizing: border-box; }
  html, body { width: 1200px; height: 780px; overflow: hidden; }
  body {
    background: var(--backdrop);
    font-family: "Open Sans", Arial, sans-serif;
    display: flex;
    align-items: center;
    justify-content: center;
    gap: 50px;
  }
  .card {
    position: relative;
    width: 540px;
    height: 310px;
    border-radius: 24px;
    overflow: hidden;
  }
  .card-front { background: var(--white); }
  .card-back {
    background: var(--navy);
    display: flex;
    align-items: center;
    justify-content: center;
  }

  .front-band {
    position: absolute;
    left: 0;
    right: 0;
    bottom: 0;
    height: 34px;
    background: var(--navy);
    border-top: 6px solid var(--orange);
  }

  .brand {
    display: flex;
    align-items: center;
    gap: 10px;
    font-weight: 700;
    white-space: nowrap;
  }
  .brand-dot {
    border-radius: 50%;
    background: var(--orange);
    flex: none;
  }
  .front-brand {
    position: absolute;
    left: 30px;
    top: 52px;
    font-size: 22px;
    color: var(--navy);
  }
  .front-brand .brand-dot { width: 22px; height: 22px; }

  .divider {
    position: absolute;
    left: 262px;
    top: 34px;
    width: 2px;
    height: 190px;
    background: var(--orange);
  }
  .details {
    position: absolute;
    left: 282px;
    top: 34px;
    right: 16px;
    color: var(--ink);
  }
  .person-name {
    color: var(--orange);
    font-size: 22px;
    font-weight: 700;
    line-height: 1.1;
    letter-spacing: 0.2px;
  }
  .person-title {
    font-size: 13px;
    margin-top: 2px;
  }
  .address {
    font-size: 12.5px;
    line-height: 1.45;
    margin-top: 12px;
  }
  .contact-list {
    list-style: none;
    margin-top: 10px;
    font-size: 12.5px;
    line-height: 1.5;
  }
  .contact-list li { display: flex; align-items: center; gap: 7px; }
  .contact-list svg { width: 12px; height: 12px; flex: none; }

  .back-brand { font-size: 36px; color: var(--white); gap: 14px; }
  .back-brand .brand-dot { width: 34px; height: 34px; }
</style>
</head>
<body>

  <section class="card card-front" aria-label="Business card front">
    <div class="front-band"></div>

    <div class="brand front-brand">
      <span class="brand-dot"></span>
      <span class="brand-name">Lanternfield HR</span>
    </div>

    <div class="divider"></div>

    <div class="details">
      <h1 class="person-name">DANIEL REYES</h1>
      <p class="person-title">Managing Director</p>
      <p class="address">4827 Millbrook Ave Suite 230<br>Cleveland, Ohio 44987</p>
      <ul class="contact-list">
        <li>
          <svg viewBox="0 0 12 12"><path d="M2,1 L4,1 L5,4 L3.6,5 C4.3,6.6 5.4,7.7 7,8.4 L8,7 L11,8 L11,10 C11,10.6 10.6,11 10,11 C5,11 1,7 1,2 C1,1.4 1.4,1 2,1 Z" fill="var(--orange)"/></svg>
          216-555-0143
        </li>
        <li>
          <svg viewBox="0 0 12 12"><rect x="3" y="0.8" width="6" height="10.4" rx="1.2" fill="none" stroke="var(--orange)" stroke-width="1.2"/><circle cx="6" cy="9.3" r="0.7" fill="var(--orange)"/></svg>
          216-555-0192
        </li>
        <li>
          <svg viewBox="0 0 12 12"><rect x="0.8" y="2.4" width="10.4" height="7.2" rx="1" fill="var(--orange)"/><path d="M1.2,3 L6,6.6 L10.8,3" fill="none" stroke="var(--white)" stroke-width="1"/></svg>
          info@LanternfieldHR.example
        </li>
        <li>
          <svg viewBox="0 0 12 12"><circle cx="6" cy="6" r="5" fill="none" stroke="var(--orange)" stroke-width="1.2"/><ellipse cx="6" cy="6" rx="2.2" ry="5" fill="none" stroke="var(--orange)" stroke-width="1"/><path d="M1,6 L11,6" stroke="var(--orange)" stroke-width="1"/></svg>
          www.lanternfieldhr.example
        </li>
      </ul>
    </div>
  </section>

  <section class="card card-back" aria-label="Business card back">
    <div class="brand back-brand">
      <span class="brand-dot"></span>
      <span class="brand-name">Lanternfield HR</span>
    </div>
  </section>

</body>
</html>
```